Mabiboo creole shop needs a web design

We need a web design former new company based in sydney australia. Called 'Mabiboo, creole shop'.
We produce caribbean/west indies product alcohol, spirits, condiments, candies, preserved food, jams, pates.
We would like to see a design that reflect the caribbean without being tacky.
We want modern, high level design as we do high level products.

Reason: There is a lot of good proposition but I need a few more days to mature my decision. Thanks for your hard work Jorel

Industry/Entity Type

Hospitality

Number of Pages Required

1 page

Font styles to use
Decorative
Script

Requirements
Must have
• The logo, the name of the business

```html
<!DOCTYPE html>
<html lang="en">
<head>
<meta charset="utf-8">
<title>Mabiboo creole shop</title>
<link href="https://fonts.googleapis.com/css2?family=Dancing+Script:wght@600&family=Federo&family=Arimo:ital@0;1&display=swap" rel="stylesheet">
<style>
:root{
  --navy:#0f1a3a;
  --navy-deep:#0b1330;
  --blue-panel:rgba(31,46,112,0.88);
  --dark-panel:rgba(8,14,34,0.9);
  --gold:#c9a62c;
  --gold-soft:#d4b33a;
  --white:#ffffff;
  --ink:#1c2a5c;
  --muted:#6a6f80;
}
*{margin:0;padding:0;box-sizing:border-box}
html,body{width:832px;height:1200px;overflow:hidden}
body{position:relative;font-family:"Arimo",Arial,sans-serif;
  background:linear-gradient(180deg,#0d2aa0 0%,#1c3fb0 35%,#2a4a8a 62%,#3f7f96 74%,#c9b89a 84%,#bba98c 100%);}
.backdrop{position:absolute;inset:0}
.page{position:absolute;left:112px;top:25px;width:608px}
.script{font-family:"Dancing Script",cursive;font-weight:600}

.main-nav{height:41px;background:var(--navy-deep);display:flex;justify-content:center;align-items:center;gap:12px;color:var(--white);font-size:14px}
.main-nav a{color:var(--white);text-decoration:none}
.main-nav a.current{color:var(--gold);text-decoration:underline}
.main-nav .sep{color:#c8cbe0;font-weight:400}

.hero{position:relative;height:280px;display:flex}
.hero-side{width:179px}
.brand{height:162px;background:var(--white);display:flex;flex-direction:column;align-items:center;justify-content:center}
.brand-name{font-size:33px;color:var(--navy);line-height:1}
.brand-sub{font-size:13px;color:var(--navy);margin-top:4px}
.tagline{height:118px;background:var(--gold);color:var(--white);font-family:"Federo",sans-serif;text-align:center;display:flex;flex-direction:column;justify-content:center;line-height:1.2}
.tagline .l1{font-size:24px}.tagline .l2{font-size:19px}.tagline .l3{font-size:24px}
.slide{position:relative;flex:1;background:radial-gradient(circle at 28% 35%,#f0c24a 0%,#e3503a 25%,#3a9ad8 45%,transparent 60%),linear-gradient(135deg,#f5d44c,#ef6a3a 40%,#48a9df 70%,#7c4bb0)}
.dots{position:absolute;right:16px;bottom:14px;display:flex;gap:3px}
.dots span{width:7px;height:7px;border-radius:50%;background:#fff}
.dots span:first-child{background:#bbb}

.about{height:189px;background:var(--dark-panel);text-align:center;padding-top:42px}
.section-title{font-size:21px;color:var(--gold)}
.about p{width:376px;margin:16px auto 0;text-align:left;font-style:italic;font-size:8.2px;line-height:12.5px;color:#e8eaf2}

.products{position:relative;height:409px;background:var(--blue-panel)}
.products .section-title{position:absolute;top:34px;width:100%;text-align:center;color:var(--white)}
.tabs{position:absolute;top:86px;left:97px;display:flex;gap:3px}
.tabs span{background:var(--gold);color:var(--white);font-size:14px;padding:0 6px;height:22px;line-height:22px}
.tabs span.active{background:var(--white);color:var(--navy)}
.cards{position:absolute;top:132px;left:16px;display:flex;gap:14px}
.card{width:104px}
.card .frame{height:165px;background:var(--white);border:1px solid var(--gold);display:flex;align-items:center;justify-content:center}
.card .shot{width:36px;height:136px;border-radius:12px 12px 6px 6px}
.card h3{margin-top:15px;text-align:center;color:var(--white);font-size:14px;font-weight:600}
.view-all{position:absolute;top:356px;left:192px;width:224px;display:flex;align-items:center;gap:12px;color:var(--gold);font-style:italic;font-size:8px}
.view-all::before,.view-all::after{content:"";flex:1;height:1px;background:var(--gold)}

.newsletter{position:relative;height:110px;background:var(--gold)}
.band-title{font-size:20px;color:var(--white);line-height:1.2}
.signup-block{position:absolute;left:26px;top:18px}
.signup{display:flex;margin-top:10px}
.signup .field{width:238px;height:28px;border:1px solid #e3cd7a;color:#f3e6b5;font-style:italic;font-size:8px;padding-left:9px;line-height:26px}
.signup .btn{width:62px;height:28px;background:var(--white);color:var(--navy);font-size:12px;text-align:center;line-height:28px}
.divider{position:absolute;left:386px;top:18px;width:1px;height:74px;background:#b8951f}
.follow{position:absolute;left:442px;top:18px}
.social{display:flex;gap:16px;margin-top:12px;margin-left:2px}
.social span{width:20px;height:20px;border-radius:50%;background:var(--white)}

.site-footer{height:106px;background:var(--white);text-align:center;padding-top:20px}
.footer-links{font-size:8px;font-style:italic;color:var(--ink)}
.footer-links i{color:var(--gold);margin:0 5px}
.footer-mark{margin-top:14px;font-size:16px;color:var(--gold)}
.copyright{margin-top:7px;font-size:7.5px;font-style:italic;color:var(--muted)}
</style>
</head>
<body>
<div class="backdrop" role="img" aria-label="Tropical beach with palm tree, blue sky and sea"></div>
<div class="page">
  <nav class="main-nav script">
    <a class="current" href="#">Home</a><span class="sep">/</span>
    <a href="#">History</a><span class="sep">/</span>
    <a href="#">Products</a><span class="sep">/</span>
    <a href="#">Wholesale &amp; Special Events</a><span class="sep">/</span>
    <a href="#">News</a><span class="sep">/</span>
    <a href="#">Contact</a>
  </nav>

  <header class="hero">
    <div class="hero-side">
      <div class="brand script">
        <div class="brand-name">Mabiboo</div>
        <div class="brand-sub">creole shop</div>
      </div>
      <div class="tagline">
        <span class="l1">The Best</span><span class="l2">Caribbean</span><span class="l3">Creole Shop</span>
      </div>
    </div>
    <div class="slide" role="img" aria-label="Rainbow swirl lollipop among colourful candies">
      <div class="dots"><span></span><span></span><span></span></div>
    </div>
  </header>

  <section class="about">
    <h2 class="section-title script">About Us</h2>
    <p>Lorem ipsum dolor sit amet, consectetur adipiscing elit, sed do eiusmod tempor incididunt ut labore et dolore magna aliqua. Ut enim ad minim veniam, quis nostrud exercitation ullamco laboris nisi ut aliquip ex ea commodo consequat. Duis aute irure dolor in reprehenderit in voluptate velit esse cillum dolore eu fugiat nulla pariatur. Excepteur sint occaecat cupidatat non proident, sunt in culpa qui officia deserunt mollit anim id est laborum.</p>
  </section>

  <section class="products">
    <h2 class="section-title script">Our Products</h2>
    <div class="tabs script">
      <span class="active">Alcohol</span><span>Spirits</span><span>Condiments</span><span>Candies</span><span>Preserved Food</span><span>Jams</span><span>Pates</span>
    </div>
    <div class="cards">
      <div class="card"><div class="frame"><div class="shot" role="img" aria-label="Bottle of pink champagne" style="background:linear-gradient(180deg,#3a3a3a 0 12%,#f2a3a3 12% 100%)"></div></div><h3 class="script">Champagne</h3></div>
      <div class="card"><div class="frame"><div class="shot" role="img" aria-label="Bottle of dry white wine" style="background:linear-gradient(180deg,#222 0 14%,#e6e6c8 14% 100%)"></div></div><h3 class="script">Dry Wine</h3></div>
      <div class="card"><div class="frame"><div class="shot" role="img" aria-label="Bottle of semi-dry rosé wine" style="background:linear-gradient(180deg,#c8b27a 0 14%,#f4c2a0 14% 100%)"></div></div><h3 class="script">Semi-Dry Wine</h3></div>
      <div class="card"><div class="frame"><div class="shot" role="img" aria-label="Bottle of red dessert wine" style="background:linear-gradient(180deg,#b0202a 0 14%,#2a0e14 14% 100%)"></div></div><h3 class="script">Dessert Wine</h3></div>
      <div class="card"><div class="frame"><div class="shot" role="img" aria-label="Bottle of strong white wine" style="background:linear-gradient(180deg,#222 0 14%,#ecebc4 14% 100%)"></div></div><h3 class="script">Strong Wine</h3></div>
    </div>
    <div class="view-all">view all ...</div>
  </section>

  <section class="newsletter">
    <div class="signup-block">
      <h2 class="band-title script">Newsletter Signup</h2>
      <div class="signup"><div class="field">Enter your email ...</div><div class="btn script">Signup</div></div>
    </div>
    <div class="divider"></div>
    <div class="follow">
      <h2 class="band-title script">Follow Us</h2>
      <div class="social">
        <span role="img" aria-label="Social network link"></span>
        <span role="img" aria-label="Social network link"></span>
        <span role="img" aria-label="Social network link"></span>
        <span role="img" aria-label="Social network link"></span>
      </div>
    </div>
  </section>

  <footer class="site-footer">
    <div class="footer-links">About Us<i>/</i>Delivery Information<i>/</i>Privacy Policy<i>/</i>Terms &amp; Conditions<i>/</i>Customer Service<i>/</i>Contact Us<i>/</i>Returns<i>/</i>Site Map</div>
    <div class="footer-mark script">Mabiboo</div>
    <div class="copyright">Mabiboo, creole shop © 2015 All Rights Reserved</div>
  </footer>
</div>
</body>
</html>
```